Movie Showtimes Website needs an updated new look

Website = www.reelhourly.net

We want to update the look of our website. We want our website to look modern, trendy, something that was designed in 2018.

We don't need any HTML or CSS or web development. All we need is the graphical prototype, preferably in Photoshop with layers.

Most of our visitors use mobile devices. Our website is RESPONSIVE -- it is flexible to fit all screen sizes.

We will use this new logo (designed on ArtPitchly):
https://www.artpitchly.net/design/40527716

Thank you for your kind consideration.

Please find attached 3 PDF files with the current webpages:

1. Each city location has its own HOME PAGE like this:

https://www.reelhourly.net/ont/ottawa/

2. The most visited pages have movie SHOWTIMES and look like this:

https://www.reelhourly.net/theatres/filmhaus-brookmere-vip

MOVIE TITLE (poster + basic info + 4 buttons)
-- the type of the screening (ex. Regular, VUMAX, 3D, etc.)
-- individual days and showtimes

3. INFORMATION about movies:

https://www.reelhourly.net/movies/quiet-harbour-tides-2018

Thank you.

Target Market(s)

Canada and USA, target audience = ages 13-50

Industry/Entity Type

Movie

Number of Pages Required

3 page

Font styles to use
Sans Serif

Colors

Designer to choose colors to be used in the design.

Requirements
Must have
• - For the main body text (such as movie times, description, information) we prefer dark text on a light background.
• - We will use the new logo https://www.artpitchly.net/design/40527716 -- but the text Reel Hourly in the logo doesn't have to look exactly like that, it can be on the same line and have the same or different size
Should not have
• No more than 2 different fonts (ex. one font for headers and titles, another one for text)

```html
<!DOCTYPE html>
<html lang="en">
<head>
<meta charset="utf-8">
<title>Reel Hourly – Movie Times</title>
<link rel="stylesheet" href="https://fonts.googleapis.com/css2?family=Montserrat:wght@500;600;700;800&family=Open+Sans:wght@400;600;700&display=swap">
<style>
:root{
  --navy:#1c2a4a;
  --ink:#2b3550;
  --muted:#7b8497;
  --line:#e3e7ee;
  --accent:#2e9de0;
  --accent-dark:#1f7fc0;
  --bg:#f4f6f9;
  --card:#ffffff;
  --footer:#3a4352;
  --hero-a:#14305a;
  --hero-b:#1d78a8;
  --hero-c:#3fc3d6;
  --poster-pink:#f1c7cf;
}
*{box-sizing:border-box;margin:0;padding:0}
html,body{width:1200px;height:2948px;overflow:hidden}
body{font-family:"Open Sans",Arial,sans-serif;color:var(--ink);background:var(--bg);position:relative}
h1,h2,h3,.heading{font-family:"Montserrat",Arial,sans-serif}

/* hero */
.hero{position:absolute;left:0;top:0;width:1200px;height:350px;
  background:radial-gradient(ellipse at 30% 20%,rgba(255,255,255,.12),transparent 55%),
  linear-gradient(120deg,var(--hero-a) 0%,var(--hero-b) 45%,var(--hero-c) 100%)}
.brand{position:absolute;left:28px;top:24px;display:flex;align-items:center;gap:10px;color:#fff;
  font-family:"Montserrat",sans-serif;font-weight:700;font-size:20px}
.brand .dot{width:28px;height:28px;border-radius:50%;background:#fff}
.topnav{position:absolute;right:30px;top:30px;display:flex;align-items:center;gap:22px;color:#fff;font-size:14px;font-weight:600}
.hero-title{position:absolute;left:0;width:1200px;top:150px;text-align:center;color:#fff;font-size:58px;font-weight:800;letter-spacing:1px}

.choose-card{position:absolute;top:292px;width:550px;height:120px;background:var(--card);border-radius:10px;
  box-shadow:0 10px 30px rgba(20,40,80,.15);display:flex;align-items:center;justify-content:center;gap:40px}
.choose-cinema{left:40px}
.choose-movie{left:610px}
.choose-card .label{font-family:"Montserrat",sans-serif;font-weight:700;color:var(--navy);text-align:center;line-height:1.2}
.choose-card .label small{display:block;font-size:16px;font-weight:600}
.choose-card .label b{font-size:28px}

/* section headings */
.section-title{position:absolute;left:100px;display:flex;align-items:center;gap:10px;font-size:26px;font-weight:700;color:var(--navy)}
.section-title::before{content:"";width:5px;height:26px;background:var(--accent);border-radius:2px}

.view-toggle{position:absolute;left:728px;top:528px;display:flex;gap:8px}

/* movie cards */
.film-card{position:absolute;left:100px;width:672px;height:280px;background:var(--card);border-radius:6px;
  box-shadow:0 2px 10px rgba(20,40,80,.08);overflow:hidden}
.film-card .poster{position:absolute;left:14px;top:15px;width:168px;height:250px;border-radius:3px}
.film-card .title{position:absolute;left:204px;top:22px;font-size:26px;font-weight:700;color:var(--navy)}
.film-card .langs{position:absolute;left:204px;top:60px;font-size:13px;color:var(--muted)}
.film-card .meta{position:absolute;left:204px;top:100px;width:260px;font-size:13px;line-height:1.6;color:var(--ink)}
.film-card .rating{position:absolute;left:540px;top:22px;font-family:"Montserrat",sans-serif;font-weight:700;font-size:22px;color:var(--accent)}
.film-card .heart{position:absolute;left:566px;top:60px}
.film-card .actions{position:absolute;right:0;top:0;width:58px;height:280px;border-left:1px solid var(--line);display:flex;flex-direction:column}
.film-card .actions span{flex:1;display:flex;flex-direction:column;align-items:center;justify-content:center;gap:4px;
  font-size:8px;font-weight:700;color:var(--muted);letter-spacing:.5px;border-bottom:1px solid var(--line)}
.film-card .actions span:last-child{border-bottom:none}
.film-card .actions i{width:16px;height:12px;border:2px solid var(--muted);border-radius:2px}

.btn{display:inline-block;background:var(--accent);color:#fff;font-weight:600;border-radius:4px;text-align:center}
.show-all{position:absolute;left:340px;top:2095px;width:200px;height:52px;line-height:52px;font-size:14px}

/* sidebar */
.fav{position:absolute;left:820px;top:520px;width:280px;height:490px;background:var(--card);border-radius:6px;
  box-shadow:0 2px 10px rgba(20,40,80,.08);padding:24px 22px}
.fav h3{font-size:18px;font-weight:700;color:var(--navy);line-height:1.25;width:170px}
.fav .icon{position:absolute;right:22px;top:24px}
.fav ul{list-style:none;margin-top:22px}
.fav li{margin-bottom:22px}
.fav li b{display:block;font-size:15px;color:var(--navy)}
.fav li span{font-size:12px;color:var(--muted)}
.fav .btn{width:236px;height:42px;line-height:42px;font-size:13px}

.ad{position:absolute;left:820px;top:1065px;width:280px;height:480px;border-radius:4px;
  background:linear-gradient(180deg,#b92b2b 0%,#d23a33 70%,#a51f24 100%)}

.birthday{position:absolute;left:820px;top:1600px;width:280px;height:790px;background:var(--card);border-radius:6px;
  box-shadow:0 2px 10px rgba(20,40,80,.08);padding:24px 22px}
.birthday h3{font-size:18px;font-weight:700;color:var(--navy);line-height:1.25}
.birthday .icon{position:absolute;right:22px;top:24px}
.birthday ul{list-style:none;margin-top:30px}
.birthday li{display:flex;align-items:center;gap:16px;height:84px}
.birthday .avatar{width:52px;height:52px;border-radius:50%;flex:none}
.birthday b{display:block;font-size:15px;color:var(--navy)}
.birthday li span{font-size:12px;color:var(--muted)}

/* promotions */
.promo-arrows{position:absolute;left:736px;top:2208px;display:flex;gap:14px}
.promo{position:absolute;top:2260px;width:200px;text-align:center}
.promo .poster{width:200px;height:330px;border-radius:3px;
  background:linear-gradient(180deg,#f7dfe3 0%,var(--poster-pink) 55%,#e6a9b6 100%)}
.promo h4{font-family:"Montserrat",sans-serif;font-size:22px;font-weight:700;color:var(--navy);margin-top:28px}
.promo p{font-size:12px;color:var(--muted);margin-top:8px;line-height:1.5;padding:0 14px}
.promo .btn{margin-top:16px;width:70px;height:32px;line-height:32px;font-size:12px;background:var(--footer)}

/* footer */
.site-footer{position:absolute;left:0;top:2840px;width:1200px;height:108px;background:var(--footer);color:#cfd4dc;
  font-size:13px;display:flex;align-items:center;justify-content:space-between;padding:0 40px}
.site-footer .social{display:flex;gap:10px}
.site-footer .social i{width:26px;height:26px;border-radius:50%;border:2px solid #cfd4dc;display:block}
</style>
</head>
<body>

<header class="hero">
  <div class="brand"><span class="dot"></span>Reel Hourly</div>
  <nav class="topnav">
    <svg width="22" height="16" viewBox="0 0 22 16"><path d="M0 2h22M0 8h22M0 14h22" stroke="#fff" stroke-width="2.5"/></svg>
    <span>Sign Up</span><span>Sign In</span>
    <svg width="18" height="18" viewBox="0 0 18 18"><circle cx="7.5" cy="7.5" r="5.5" fill="none" stroke="#fff" stroke-width="2.2"/><path d="M12 12l5 5" stroke="#fff" stroke-width="2.2"/></svg>
  </nav>
  <h1 class="hero-title">MOVIE TIMES</h1>
</header>

<a class="choose-card choose-cinema">
  <svg width="110" height="70" viewBox="0 0 110 70" fill="none" stroke="#2e9de0" stroke-width="3">
    <rect x="8" y="4" width="94" height="34" rx="2"/>
    <path d="M4 50h102M10 58h90M16 66h78"/>
  </svg>
  <div class="label"><small>CHOOSE A</small><b>CINEMA</b></div>
</a>
<a class="choose-card choose-movie">
  <div class="label"><small>CHOOSE A</small><b>MOVIE</b></div>
  <svg width="80" height="70" viewBox="0 0 80 70" fill="none" stroke="#2e9de0" stroke-width="3">
    <circle cx="34" cy="34" r="28"/><circle cx="34" cy="20" r="6"/><circle cx="34" cy="48" r="6"/><circle cx="20" cy="34" r="6"/><circle cx="48" cy="34" r="6"/>
    <path d="M62 34c6 8 10 18 16 22"/>
  </svg>
</a>

<h2 class="section-title" style="top:518px">NEW MOVIES THIS WEEK</h2>
<div class="view-toggle">
  <svg width="14" height="14" viewBox="0 0 14 14" fill="#2e9de0"><rect width="6" height="6"/><rect x="8" width="6" height="6"/><rect y="8" width="6" height="6"/><rect x="8" y="8" width="6" height="6"/></svg>
  <svg width="14" height="14" viewBox="0 0 14 14" fill="#7b8497"><rect width="14" height="3"/><rect y="5.5" width="14" height="3"/><rect y="11" width="14" height="3"/></svg>
</div>

<article class="film-card" style="top:590px">
  <div class="poster" role="img" aria-label="Poster for Havildar Arjan Dev" style="background:linear-gradient(180deg,#8a7a5c,#4b4234)"></div>
  <h3 class="title">Havildar Arjan Dev</h3>
  <p class="langs">[Hindi, Tamil, Telugu]</p>
  <p class="meta">2h18 • War drama • Harnek Dhillon &amp; Rina Kapoor</p>
  <span class="rating">★ 7.9</span>
  <svg class="heart" width="20" height="18" viewBox="0 0 20 18"><path d="M10 17S1 11 1 5.5A4.5 4.5 0 0 1 10 3a4.5 4.5 0 0 1 9 2.5C19 11 10 17 10 17z" fill="none" stroke="#7b8497" stroke-width="1.8"/></svg>
  <div class="actions"><span><i></i>TRAILER</span><span><i></i>TIMES</span><span><i></i>INFO</span><span><i></i>VIDEOS</span><span><i></i>REVIEWS</span></div>
</article>

<article class="film-card" style="top:890px">
  <div class="poster" role="img" aria-label="Poster for Curfew Breakers" style="background:linear-gradient(180deg,#cfd6dd,#7c8895)"></div>
  <h3 class="title">Curfew Breakers</h3>
  <p class="langs">[Hindi, Tamil, Telugu]</p>
  <p class="meta">2h18 • War drama • Harnek Dhillon &amp; Rina Kapoor</p>
  <span class="rating">★ 7.9</span>
  <svg class="heart" width="20" height="18" viewBox="0 0 20 18"><path d="M10 17S1 11 1 5.5A4.5 4.5 0 0 1 10 3a4.5 4.5 0 0 1 9 2.5C19 11 10 17 10 17z" fill="none" stroke="#7b8497" stroke-width="1.8"/></svg>
  <div class="actions"><span><i></i>TRAILER</span><span><i></i>TIMES</span><span><i></i>INFO</span><span><i></i>VIDEOS</span><span><i></i>REVIEWS</span></div>
</article>

<article class="film-card" style="top:1190px">
  <div class="poster" role="img" aria-label="Poster for The Comeback Season" style="background:linear-gradient(180deg,#9fc6e3,#4d7fa6)"></div>
  <h3 class="title">The Comeback Season</h3>
  <p class="langs">[Hindi, Tamil, Telugu]</p>
  <p class="meta">2h18 • War drama • Harnek Dhillon &amp; Rina Kapoor</p>
  <span class="rating">★ 7.9</span>
  <svg class="heart" width="20" height="18" viewBox="0 0 20 18"><path d="M10 17S1 11 1 5.5A4.5 4.5 0 0 1 10 3a4.5 4.5 0 0 1 9 2.5C19 11 10 17 10 17z" fill="none" stroke="#7b8497" stroke-width="1.8"/></svg>
  <div class="actions"><span><i></i>TRAILER</span><span><i></i>TIMES</span><span><i></i>INFO</span><span><i></i>VIDEOS</span><span><i></i>REVIEWS</span></div>
</article>

<article class="film-card" style="top:1490px">
  <div class="poster" role="img" aria-label="Poster for La Chanteuse" style="background:linear-gradient(180deg,#5b5246,#2a251f)"></div>
  <h3 class="title">La Chanteuse</h3>
  <p class="langs">[Hindi, Tamil, Telugu]</p>
  <p class="meta">2h18 • War drama • Harnek Dhillon &amp; Rina Kapoor</p>
  <span class="rating">★ 7.9</span>
  <svg class="heart" width="20" height="18" viewBox="0 0 20 18"><path d="M10 17S1 11 1 5.5A4.5 4.5 0 0 1 10 3a4.5 4.5 0 0 1 9 2.5C19 11 10 17 10 17z" fill="none" stroke="#7b8497" stroke-width="1.8"/></svg>
  <div class="actions"><span><i></i>TRAILER</span><span><i></i>TIMES</span><span><i></i>INFO</span><span><i></i>VIDEOS</span><span><i></i>REVIEWS</span></div>
</article>

<article class="film-card" style="top:1790px">
  <div class="poster" role="img" aria-label="Poster for Duchesse" style="background:linear-gradient(180deg,#d9c9a8,#8d6b4a)"></div>
  <h3 class="title">Duchesse</h3>
  <p class="langs">[Hindi, Tamil, Telugu]</p>
  <p class="meta">2h18 • War drama • Harnek Dhillon &amp; Rina Kapoor</p>
  <span class="rating">★ 7.9</span>
  <svg class="heart" width="20" height="18" viewBox="0 0 20 18"><path d="M10 17S1 11 1 5.5A4.5 4.5 0 0 1 10 3a4.5 4.5 0 0 1 9 2.5C19 11 10 17 10 17z" fill="none" stroke="#7b8497" stroke-width="1.8"/></svg>
  <div class="actions"><span><i></i>TRAILER</span><span><i></i>TIMES</span><span><i></i>INFO</span><span><i></i>VIDEOS</span><span><i></i>REVIEWS</span></div>
</article>

<a class="btn show-all">Show All Playing Movies</a>

<aside class="fav">
  <h3>MY FAVOURITE CINEMAS</h3>
  <svg class="icon" width="40" height="32" viewBox="0 0 40 32" fill="none" stroke="#2e9de0" stroke-width="2"><rect x="2" y="2" width="36" height="16" rx="1"/><path d="M2 24h36M6 30h28"/></svg>
  <ul>
    <li><b>Lantern Row Cinema</b><span>418 Ferncliff Ave, Ottawa</span></li>
    <li><b>Filmhaus Brookmere VIP</b><span>290 Marsh Ave, Ottawa</span></li>
    <li><b>Bellhaven Theatre Ottawa</b><span>1074 Birch Street, Ottawa</span></li>
    <li><b>CinéÉtoile Gatineau</b><span>55 Boul. du Plateau, Gatineau, QC</span></li>
    <li><b>Maplewood Family Cinema</b><span>710 Brookline Ave, Ottawa</span></li>
  </ul>
  <a class="btn">Choose My Favourite Cinemas</a>
</aside>

<div class="ad" role="img" aria-label="Advertisement banner for a business news service"></div>

<aside class="birthday">
  <h3>HAPPY<br>BIRTHDAY!</h3>
  <svg class="icon" width="30" height="36" viewBox="0 0 30 36" fill="none" stroke="#2e9de0" stroke-width="2"><path d="M15 2v6"/><rect x="9" y="8" width="12" height="10"/><rect x="3" y="18" width="24" height="16"/></svg>
  <ul>
    <li><span class="avatar" role="img" aria-label="Portrait of Anders Lindqvist" style="background:#c9b7a4"></span><div><b>Anders Lindqvist</b><span>89 today!</span></div></li>
    <li><span class="avatar" role="img" aria-label="Portrait of Julien Marchand" style="background:#a89486"></span><div><b>Julien Marchand</b><span>45 today!</span></div></li>
    <li><span class="avatar" role="img" aria-label="Portrait of Dale Whitaker" style="background:#8c7a6b"></span><div><b>Dale Whitaker</b><span>66 today!</span></div></li>
    <li><span class="avatar" role="img" aria-label="Portrait of Mara Quinlan" style="background:#d1a98e"></span><div><b>Mara Quinlan</b><span>41 today!</span></div></li>
    <li><span class="avatar" role="img" aria-label="Portrait of Owen Castell" style="background:#7d6e62"></span><div><b>Owen Castell</b><span>37 today!</span></div></li>
    <li><span class="avatar" role="img" aria-label="Portrait of Priya Halden" style="background:#b99a83"></span><div><b>Priya Halden</b><span>19 today!</span></div></li>
    <li><span class="avatar" role="img" aria-label="Portrait of Lena Morrow" style="background:#9a7f6c"></span><div><b>Lena Morrow</b><span>35 today!</span></div></li>
    <li><span class="avatar" role="img" aria-label="Lantern Row Cinema photo" style="background:#6f7d8c"></span><div><b>Lantern Row Cinema</b><span>71 today!</span></div></li>
  </ul>
</aside>

<h2 class="section-title" style="top:2200px">PROMOTIONS</h2>
<div class="promo-arrows">
  <svg width="18" height="14" viewBox="0 0 18 14"><path d="M17 7H2M7 1L1 7l6 6" fill="none" stroke="#7b8497" stroke-width="2"/></svg>
  <svg width="18" height="14" viewBox="0 0 18 14"><path d="M1 7h15M11 1l6 6-6 6" fill="none" stroke="#2e9de0" stroke-width="2"/></svg>
</div>

<div class="promo" style="left:100px">
  <div class="poster" role="img" aria-label="Promotional poster for Bright Side Up"></div>
  <h4>Bright Side Up</h4>
  <p>Win free tickets to the Ottawa advance screening!</p>
  <a class="btn">Enter</a>
</div>
<div class="promo" style="left:340px">
  <div class="poster" role="img" aria-label="Promotional poster for Bright Side Up"></div>
  <h4>Bright Side Up</h4>
  <p>Win free tickets to the Ottawa advance screening!</p>
  <a class="btn">Enter</a>
</div>
<div class="promo" style="left:580px">
  <div class="poster" role="img" aria-label="Promotional poster for Bright Side Up"></div>
  <h4>Bright Side Up</h4>
  <p>Win free tickets to the Ottawa advance screening!</p>
  <a class="btn">Enter</a>
</div>

<footer class="site-footer">
  <span>English | Français</span>
  <span>© 1995-2018 Reel Hourly Inc. Terms and Privacy Policy</span>
  <div class="social" aria-hidden="true"><i></i><i></i><i></i><i></i></div>
</footer>

</body>
</html>
```